Business Cards for Communications Technology Company

We are an innovative software company based in Tropical North Queensland, Australia. We have several brands with a focus on communications software for businesses. We are looking for a business card that is very innovate and creative whilst still remaining professional on a corporate level.

Our internal culture is very progressive and expresses a blend between the clarity of our natural surroundings and the highly technological industry we work in. Our current branding blends a modern minimalist typeface with the desire to push the boundaries in the way we communicate.

This is a corporate level business card for the communications software industry and may possibly also encompass our brands PelNetwork, PelCopy, PelPost and our B2B marketing service—with our companies name being Tarvix Holdings. Showing other brands on the business card is optional not compulsory.

Technical notes:

-We will attach all logo's and some examples of our corporate branding
- Would be willing to print with various papers, embossed, metallic ink, curved edges etc. in a standard business card size

Sample content:

Dorian Malcott
Senior Account Manager
Phone: 1300 482 916 / +617 4385 2604
Email: d.malcott@tarvix.com.au
Web: www.tarvix.com.au

Sincerely,
Tarvix Holdings.

```html
<!DOCTYPE html>
<html lang="en">
<head>
<meta charset="utf-8">
<title>Tarvix Holdings — Business Card</title>
<link rel="stylesheet" href="https://fonts.googleapis.com/css2?family=Lato:wght@400;700;900&display=swap">
<style>
  :root {
    --stage: #000000;
    --card-dark: #333333;
    --card-dark-edge: #262626;
    --card-light: #ffffff;
    --brand-green: #7ac143;
    --brand-blue: #3a6fb8;
    --brand-orange: #ef6a22;
    --text-light: #ffffff;
    --text-dark: #4a4a4a;
    --rule: #d9d9d9;
  }
  * { margin: 0; padding: 0; box-sizing: border-box; }
  html, body {
    width: 1189px; height: 1200px; overflow: hidden;
    background: var(--stage);
    font-family: "Lato", sans-serif;
  }
  .card {
    position: absolute; left: 171px;
    width: 856px; height: 489px; overflow: hidden;
    background: radial-gradient(ellipse at 50% 45%, var(--card-dark) 0%, var(--card-dark-edge) 100%);
  }
  .card--front { top: 66px; }
  .card--back { top: 625px; }

  .wordmark {
    position: absolute; display: flex; align-items: center; gap: 14px;
    font-weight: 700; white-space: nowrap;
  }
  .wordmark__dot { border-radius: 50%; background: var(--brand-green); flex: none; }
  .card--front .wordmark {
    left: 50%; top: 218px; transform: translateX(-50%);
    font-size: 58px; color: var(--text-light);
  }
  .card--front .wordmark__dot { width: 46px; height: 46px; }

  .brand-row {
    position: absolute; left: 0; right: 0; top: 380px;
    display: flex; justify-content: center; align-items: center; gap: 30px;
    font-size: 33px; font-weight: 700;
  }
  .brand-row__divider { width: 2px; height: 44px; background: var(--text-light); }
  .brand--post { color: var(--brand-blue); }
  .brand--copy { color: var(--brand-green); }
  .brand--network { color: var(--brand-orange); }

  .swoosh { position: absolute; inset: 0; width: 100%; height: 100%; }
  .card--back .wordmark {
    left: 617px; top: 68px; transform: translateX(-50%);
    font-size: 46px; color: var(--text-dark);
  }
  .card--back .wordmark__dot { width: 38px; height: 38px; }

  .person { position: absolute; left: 40px; top: 310px; }
  .person__name { font-size: 30px; font-weight: 700; color: var(--text-light); line-height: 1; }
  .person__title { font-size: 23px; font-weight: 400; color: var(--brand-green); line-height: 1.2; margin-top: 2px; }
  .rule { position: absolute; left: 40px; width: 778px; top: 378px; height: 2px; background: var(--rule); }
  .contacts { position: absolute; left: 40px; top: 391px; list-style: none; }
  .contacts__item {
    display: flex; align-items: center; gap: 9px;
    font-size: 23px; color: var(--text-light); height: 29px;
  }
  .contacts__icon { width: 28px; height: 28px; flex: none; }
  .web {
    position: absolute; right: 38px; top: 421px;
    font-size: 23px; color: var(--text-light);
  }
  .web__domain { color: var(--brand-green); }
</style>
</head>
<body>
  <section class="card card--front" aria-label="Card front">
    <div class="wordmark"><span class="wordmark__dot"></span>Tarvix Holdings</div>
    <div class="brand-row">
      <span class="brand brand--post">PelPost</span>
      <span class="brand-row__divider"></span>
      <span class="brand brand--copy">PelCopy</span>
      <span class="brand-row__divider"></span>
      <span class="brand brand--network">PelNetwork</span>
    </div>
  </section>

  <section class="card card--back" aria-label="Card back">
    <svg class="swoosh" viewBox="0 0 1050 600" preserveAspectRatio="none" aria-hidden="true">
      <path d="M376 0 C400 170 520 250 680 305 C840 360 970 380 1050 460 L1050 0 Z" fill="var(--brand-green)"/>
      <path d="M434 0 C460 150 560 230 700 285 C850 345 980 370 1050 455 L1050 0 Z" fill="var(--card-light)"/>
    </svg>
    <div class="wordmark"><span class="wordmark__dot"></span>Tarvix Holdings</div>

    <div class="person">
      <p class="person__name">Dorian Malcott</p>
      <p class="person__title">Senior Account Manager</p>
    </div>
    <div class="rule"></div>
    <ul class="contacts">
      <li class="contacts__item">
        <svg class="contacts__icon" viewBox="0 0 28 28" aria-hidden="true">
          <circle cx="14" cy="14" r="12.5" fill="none" stroke="var(--brand-green)" stroke-width="2.5"/>
          <path d="M8 11 Q14 7 20 11 L19 13 L16 12 L16 11 L12 11 L12 12 L9 13 Z" fill="var(--brand-green)"/>
          <rect x="9" y="13" width="10" height="7" rx="1.5" fill="var(--brand-green)"/>
        </svg>
        <span>1300 482 916 /+617 4385 2604</span>
      </li>
      <li class="contacts__item">
        <svg class="contacts__icon" viewBox="0 0 28 28" aria-hidden="true">
          <circle cx="14" cy="14" r="12.5" fill="none" stroke="var(--brand-green)" stroke-width="2.5"/>
          <rect x="8" y="9.5" width="12" height="9" rx="1" fill="var(--brand-green)"/>
          <path d="M8.5 10 L14 14.5 L19.5 10" fill="none" stroke="var(--card-dark)" stroke-width="1.3"/>
        </svg>
        <span>d.malcott@tarvix.com.au</span>
      </li>
    </ul>
    <p class="web">www.<span class="web__domain">tarvix</span>.com.au</p>
  </section>
</body>
</html>
```